Flyer Design Project

New pest control company starting in southern maryland with the name Pest Raiders. We are going off the same kind of concept as the Shadowchasers. Our slogan is.....killing bugs its what we do best. The telephone number for the business is 240 555 0187. About us....we are a new exciting brand coming to the southern Maryland area offering a safer and more effective solution to pest control. We strive to use the safest and most effective products while providing the best and most effective service. We are a local based company with over ten years experience. As a special to all new Maryland clients we are offering the following coupons. 1. New customers get $100 off initial service which includes a termite inspection with a one year contract. 2. With a one year contract get 50 % off mosquito treatments normally $100 now $50 lawn treatments are done every 30 days. 3. Sign up before May 30th and receive lawn treatments for ticks and fleas up to half an acre included at no additional charge with a signed 1 year contract

Industry/Entity Type

```html
<!DOCTYPE html>
<html lang="en">
<head>
<meta charset="utf-8">
<title>Pest Raiders Flyer</title>
<link rel="stylesheet" href="https://fonts.googleapis.com/css2?family=Raleway:wght@700;800&family=Lato:wght@700&family=Montserrat:wght@600&family=Oswald:wght@400;500&display=swap">
<style>
  :root {
    --page-bg: #c9c9cc;
    --deep-blue: #0d1a3a;
    --mid-blue: #1f4a86;
    --glow-violet: #5b3b8c;
    --white: #ffffff;
    --ribbon-pink: #d81e55;
    --ribbon-dark: #a3123b;
    --coupon-yellow: #ffe53b;
    --neon-pink: #ff3f7a;
    --band-black: #050505;
  }
  * { margin: 0; padding: 0; box-sizing: border-box; }
  html, body { width: 1200px; height: 1200px; overflow: hidden; background: var(--page-bg); }
  .flyer {
    position: absolute; left: 136px; top: 0; width: 927px; height: 1200px;
    background: linear-gradient(180deg, #26324f 0%, #2a4d8a 40%, #1d3d78 60%, #112a52 80%, #0a1a33 100%);
    overflow: hidden; color: var(--white);
  }
  .hero-photo {
    position: absolute; left: 0; top: 0; width: 927px; height: 470px;
    background:
      radial-gradient(ellipse at 18% 25%, rgba(190,140,90,.85) 0%, rgba(190,140,90,0) 35%),
      radial-gradient(ellipse at 50% 30%, rgba(150,110,80,.8) 0%, rgba(150,110,80,0) 28%),
      radial-gradient(ellipse at 84% 22%, rgba(40,40,50,.9) 0%, rgba(40,40,50,0) 22%),
      radial-gradient(ellipse at 78% 55%, rgba(230,140,180,.55) 0%, rgba(230,140,180,0) 30%),
      radial-gradient(ellipse at 10% 55%, rgba(230,140,180,.45) 0%, rgba(230,140,180,0) 28%),
      linear-gradient(180deg, #4a5a78 0%, #3b4f85 60%, rgba(42,77,138,0) 100%);
  }
  .grass-photo {
    position: absolute; left: 0; bottom: 0; width: 927px; height: 520px;
    background: linear-gradient(180deg, rgba(10,26,51,0) 0%, rgba(30,80,120,.5) 45%, #081628 100%);
  }
  .brand-name {
    position: absolute; left: 0; top: 290px; width: 927px; text-align: center;
    font-family: 'Raleway', sans-serif; font-weight: 800; font-size: 112px;
    letter-spacing: 2px; text-transform: uppercase; line-height: 1;
  }
  .slogan {
    position: absolute; left: 0; top: 440px; width: 927px; text-align: center;
    font-family: 'Raleway', sans-serif; font-weight: 800; font-size: 35px;
  }
  .about {
    position: absolute; left: 90px; top: 487px; width: 747px; text-align: center;
    font-family: 'Lato', sans-serif; font-weight: 700; font-size: 19.5px; line-height: 24.5px;
  }
  .offer-band { position: absolute; left: 70px; top: 596px; width: 760px; height: 116px; }
  .offer-band-text {
    position: absolute; left: 0; top: 603px; width: 927px; text-align: center;
    font-family: 'Raleway', sans-serif; font-weight: 700; font-size: 34px; line-height: 44px;
  }
  .ribbon { position: absolute; top: 725px; width: 390px; height: 94px; }
  .ribbon--left { left: 46px; }
  .ribbon--right { left: 490px; }
  .ribbon svg { position: absolute; left: 0; top: 0; }
  .ribbon-title {
    position: absolute; left: 0; top: 4px; width: 390px; text-align: center;
    font-family: 'Raleway', sans-serif; font-weight: 800; font-size: 38px; color: var(--coupon-yellow);
  }
  .ribbon-title sup { font-size: 18px; vertical-align: 18px; }
  .ribbon-sub {
    position: absolute; left: 0; top: 51px; width: 390px; text-align: center;
    font-family: 'Montserrat', sans-serif; font-weight: 600; font-size: 17px;
  }
  .ribbon-sub--spaced { letter-spacing: 3px; }
  .ribbon-sub--tight { font-size: 16px; }
  .coupon-terms {
    position: absolute; top: 824px; width: 330px; text-align: center;
    font-family: 'Montserrat', sans-serif; font-weight: 600; font-size: 13.5px; line-height: 18.5px;
    text-transform: uppercase;
  }
  .coupon-terms--left { left: 78px; }
  .coupon-terms--right { left: 523px; }
  .deadline {
    position: absolute; left: 40px; top: 918px; width: 847px; text-align: center;
    font-family: 'Oswald', sans-serif; font-weight: 400; font-size: 30px; line-height: 33px;
    text-transform: uppercase; transform: scaleX(.88);
  }
  .deadline sup { font-size: 15px; vertical-align: 13px; }
  .contact {
    position: absolute; left: 0; top: 1038px; width: 927px; text-align: center;
    font-family: 'Oswald', sans-serif; font-weight: 500; color: var(--neon-pink); white-space: nowrap;
  }
  .contact-phone { font-size: 76px; letter-spacing: -1px; }
  .contact-divider { font-size: 44px; margin: 0 8px; vertical-align: 6px; }
  .contact-web { font-size: 40px; vertical-align: 6px; }
</style>
</head>
<body>
  <main class="flyer">
    <div class="hero-photo" role="img" aria-label="Close-up photographs of a termite, a mosquito and a tick with pink electric lightning"></div>
    <div class="grass-photo" role="img" aria-label="Dark blue-tinted photograph of grass blades"></div>

    <h1 class="brand-name">Pest Raiders</h1>
    <p class="slogan">KILLING BUGS ITS WHAT WE DO BEST</p>
    <p class="about">we are a new exciting brand coming to the southern Maryland area offering a safer and more effective solution to pest control. We strive to use the safest and most effective products while providing the best and most effective service. We are a local based company with over ten years experience.</p>

    <svg class="offer-band" viewBox="0 0 760 116" aria-hidden="true">
      <path d="M14 6 L748 0 L736 30 L756 58 L740 86 L752 114 L8 110 L22 84 L0 58 L18 32 Z" fill="var(--band-black)"/>
    </svg>
    <p class="offer-band-text">OFFERING SPECIAL COUPONS TO ALL<br>NEW MARYLAND CLIENTS!</p>

    <div class="ribbon ribbon--left">
      <svg width="390" height="94" viewBox="0 0 390 94" aria-hidden="true">
        <polygon points="0,24 60,24 60,94 0,94 18,58" fill="var(--ribbon-dark)"/>
        <polygon points="390,24 330,24 330,94 390,94 372,58" fill="var(--ribbon-dark)"/>
        <rect x="40" y="0" width="310" height="76" fill="var(--ribbon-pink)"/>
      </svg>
      <div class="ribbon-title">$100<sup>*</sup> Off</div>
      <div class="ribbon-sub ribbon-sub--spaced">INITIAL SERVICE</div>
    </div>

    <div class="ribbon ribbon--right">
      <svg width="390" height="94" viewBox="0 0 390 94" aria-hidden="true">
        <polygon points="0,24 60,24 60,94 0,94 18,58" fill="var(--ribbon-dark)"/>
        <polygon points="390,24 330,24 330,94 390,94 372,58" fill="var(--ribbon-dark)"/>
        <rect x="40" y="0" width="310" height="76" fill="var(--ribbon-pink)"/>
      </svg>
      <div class="ribbon-title">50%<sup>*</sup> Off</div>
      <div class="ribbon-sub ribbon-sub--tight">WITH A ONE YEAR CONTRACT</div>
    </div>

    <p class="coupon-terms coupon-terms--left">New customers get $100 off initial service which includes a termite inspection with a one year contract</p>
    <p class="coupon-terms coupon-terms--right">With a one year contract get 50 % off mosquito treatments normally $100 now $50 lawn treatments are done every 30 days</p>

    <p class="deadline">Sign up before May 30<sup>th</sup> and receive lawn treatments for ticks and fleas up to half an acre included at no additional charge with a signed 1 year contract.</p>

    <p class="contact">
      <span class="contact-phone">240 555 0187</span><span class="contact-divider">|</span><span class="contact-web">WWW.PESTRAIDERS-MD.COM</span>
    </p>
  </main>
</body>
</html>
```